Tarjetas de visita para empresa de aluminio

Empresa con mas de 40 años vendiendo perfiles de aluminio.
Somos fábrica y almacén, queremos renovar la tarjeta de presentación de nuestros comerciales dando una imgen innovadora y tecnógica mezclado con la calidez del respeto al medio ambiente.
Añado el logo de la empresa y actual cara trasera de la tarjeta de visita, el logo es el simbolo WM y la marca TRAVENIC EXTRUSION, la frase 2extrusion y lacado de aluminio" debe cambiarse por "Diseño, extrusión, lacado, anodizado y mecanizado de precisión de aluminio" o en su defecto incluir todos esos servicios que hacemos o una frase mas pegadiza.

We are an aluminium factory, we produce and stock profiles of aluminium.
we want to renew visit card of our sellers, we are looking for something that show innovation, tecnology and environment respect.
Upload our actual logo and back of visit card, logo WM and brand TRAVENIC EXTRUSION must be keept.
Text "Extrusion y lacado de aluminio" must be changed for "Diseño, extrusion, lacado, anodizado y mecanizado de precisión de aluminio" or something like that

```html
<!DOCTYPE html>
<html lang="es">
<head>
<meta charset="utf-8">
<title>TRAVENIC EXTRUSION – Tarjetas de visita</title>
<link rel="stylesheet" href="https://fonts.googleapis.com/css2?family=Rajdhani:wght@400;500;600;700&family=Arimo:wght@400&display=swap">
<style>
  :root {
    --ink-dark: #222123;
    --steel-blue: #07527c;
    --icon-blue: #0d5c8a;
    --silver: #c9ccd0;
    --text-light: #eef1f4;
    --text-grey: #a3a6aa;
    --name-grey: #b7b9bc;
    --page: #ffffff;
    --label: #333333;
  }
  * { margin: 0; padding: 0; box-sizing: border-box; }
  html, body { width: 1200px; height: 695px; overflow: hidden; background: var(--page); }
  .sheet { position: relative; width: 1200px; height: 695px; font-family: "Rajdhani", sans-serif; }

  .card {
    position: absolute; width: 384px; height: 208px; overflow: hidden;
    box-shadow: 14px 18px 16px rgba(0,0,0,.35);
  }
  .card__bg { position: absolute; inset: 0; width: 100%; height: 100%; }
  .card--v1 { --base: var(--ink-dark); --accent: var(--steel-blue); }
  .card--v2 { --base: var(--steel-blue); --accent: var(--ink-dark); }
  .card { background: var(--base); }
  .card__bg polygon { fill: var(--accent); }

  .card--front-v1 { left: 138px; top: 129px; }
  .card--back-v1  { left: 139px; top: 371px; }
  .card--front-v2 { left: 599px; top: 129px; }
  .card--back-v2  { left: 600px; top: 371px; }

  .brand-mark { position: absolute; border-radius: 50%; background: var(--silver); }
  .brand-name { position: absolute; text-align: center; color: #ffffff; font-weight: 700; letter-spacing: .06em; white-space: nowrap; }

  .front .brand-mark { width: 58px; height: 58px; left: 177px; top: 36px; }
  .front .brand-name { left: 6px; width: 400px; top: 109px; font-size: 20px; line-height: 24px; }
  .tagline {
    position: absolute; left: 6px; width: 400px; top: 137px;
    text-align: center; font-size: 12px; line-height: 17px; letter-spacing: .14em;
    font-weight: 500; text-transform: uppercase;
  }
  .card--v1 .tagline { color: var(--text-grey); }
  .card--v2 .tagline { color: var(--text-light); }

  .back .brand-mark { width: 46px; height: 46px; left: 80px; top: 22px; }
  .back .brand-name { left: 0; width: 250px; top: 86px; font-size: 13px; line-height: 18px; }

  .person { position: absolute; right: 18px; top: 28px; text-align: right; }
  .person__name { font-size: 15px; line-height: 18px; font-weight: 600; color: var(--name-grey); letter-spacing: .02em; }
  .person__role { font-size: 12px; line-height: 16px; font-weight: 400; color: var(--name-grey); letter-spacing: .04em; }

  .contact { position: absolute; list-style: none; font-size: 11px; font-weight: 500; }
  .contact li { display: flex; align-items: center; height: 15px; margin-bottom: 0.2px; white-space: nowrap; }
  .contact svg { width: 11px; height: 11px; flex: none; margin-right: 6px; }
  .contact .no-icon { width: 11px; margin-right: 6px; flex: none; }
  .contact--postal { left: 16px; top: 129px; }
  .contact--direct { right: 18px; top: 129px; }
  .contact--direct li { justify-content: flex-end; }
  .wide { letter-spacing: .18em; }
  .wider { letter-spacing: .32em; }

  .card--v1 .contact { color: var(--text-grey); }
  .card--v2 .contact--postal { color: var(--text-light); }
  .card--v2 .contact--direct { color: #ffffff; }
  .icon-disc { fill: var(--icon-blue); }
  .card--v2 .contact--postal .icon-disc { fill: #0a3f60; }
  .icon-glyph { fill: none; stroke: var(--base); stroke-width: 1.1; }
  .card--v2 .contact--direct .icon-glyph { stroke: var(--ink-dark); }

  .version-label { position: absolute; font-family: "Arimo", sans-serif; font-size: 14px; color: var(--label); }
  .version-label--1 { left: 302px; top: 621px; }
  .version-label--2 { left: 768px; top: 615px; }
</style>
</head>
<body>
<main class="sheet">

  <!-- Version 1 front -->
  <section class="card card--v1 front card--front-v1">
    <svg class="card__bg" viewBox="0 0 384 208" preserveAspectRatio="none"><polygon points="0,0 115,0 0,208"/></svg>
    <div class="brand-mark"></div>
    <div class="brand-name">TRAVENIC EXTRUSION</div>
    <p class="tagline">Diseño, extrusión, lacado, anodizado<br>y mecanizado de precisión de aluminio</p>
  </section>

  <!-- Version 1 back -->
  <section class="card card--v1 back card--back-v1">
    <svg class="card__bg" viewBox="0 0 384 208" preserveAspectRatio="none"><polygon points="157,0 384,0 384,208 273,208"/></svg>
    <div class="brand-mark"></div>
    <div class="brand-name">TRAVENIC EXTRUSION</div>
    <div class="person">
      <div class="person__name">MARCOS RUEDA LLORENTE</div>
      <div class="person__role">COMERCIAL</div>
    </div>
    <ul class="contact contact--postal">
      <li><svg viewBox="0 0 12 12"><circle class="icon-disc" cx="6" cy="6" r="6"/><path class="icon-glyph" d="M6 9.5 C4 7 3.6 6 3.6 5 a2.4 2.4 0 0 1 4.8 0 c0 1-.4 2-2.4 4.5z"/></svg><span class="wide">Pol. Ind. Norvalle - C/4 Nº 22</span></li>
      <li><span class="no-icon"></span><span>41720 VILLANORTE DEL RÍO (Sevilla)</span></li>
      <li><svg viewBox="0 0 12 12"><circle class="icon-disc" cx="6" cy="6" r="6"/><path class="icon-glyph" d="M3.2 4h5.6v4H3.2z M3.2 4 6 6.3 8.8 4"/></svg><span class="wider">Apartado de Correos 254</span></li>
      <li><svg viewBox="0 0 12 12"><circle class="icon-disc" cx="6" cy="6" r="6"/><circle class="icon-glyph" cx="6" cy="6" r="1.5"/><path class="icon-glyph" d="M7.5 4.5v2.3c0 .9 1.3.9 1.3-.6A2.8 2.8 0 1 0 7.6 8.4"/></svg><span class="wider">marcosrueda@travenic.com</span></li>
    </ul>
    <ul class="contact contact--direct">
      <li><svg viewBox="0 0 12 12"><circle class="icon-disc" cx="6" cy="6" r="6"/><rect class="icon-glyph" x="4.2" y="2.7" width="3.6" height="6.6" rx=".6"/></svg><span class="wide">611 48 27 53</span></li>
      <li><svg viewBox="0 0 12 12"><circle class="icon-disc" cx="6" cy="6" r="6"/><path class="icon-glyph" d="M4 3c-1 .8-.8 2.4.6 4s3 2.1 3.9 1.2L7.5 7l-.9.5C5.8 7 5 6.2 4.6 5.3l.6-.8z"/></svg><span class="wide">954 72 18 40</span></li>
      <li><svg viewBox="0 0 12 12"><circle class="icon-disc" cx="6" cy="6" r="6"/><path class="icon-glyph" d="M4.2 5V3h3.6v2 M3 5h6v3H3z M4.2 7.3h3.6V9H4.2z"/></svg><span class="wide">954 72 18 41</span></li>
      <li><svg viewBox="0 0 12 12"><circle class="icon-disc" cx="6" cy="6" r="6"/><circle class="icon-glyph" cx="6" cy="6" r="3"/><path class="icon-glyph" d="M3 6h6 M6 3c-1.5 2-1.5 4 0 6 M6 3c1.5 2 1.5 4 0 6"/></svg><span>www.travenic.com</span></li>
    </ul>
  </section>

  <!-- Version 2 front -->
  <section class="card card--v2 front card--front-v2">
    <svg class="card__bg" viewBox="0 0 384 208" preserveAspectRatio="none"><polygon points="0,0 115,0 0,208"/></svg>
    <div class="brand-mark"></div>
    <div class="brand-name">TRAVENIC EXTRUSION</div>
    <p class="tagline">Diseño, extrusión, lacado, anodizado<br>y mecanizado de precisión de aluminio</p>
  </section>

  <!-- Version 2 back -->
  <section class="card card--v2 back card--back-v2">
    <svg class="card__bg" viewBox="0 0 384 208" preserveAspectRatio="none"><polygon points="157,0 384,0 384,208 273,208"/></svg>
    <div class="brand-mark"></div>
    <div class="brand-name">TRAVENIC EXTRUSION</div>
    <div class="person">
      <div class="person__name">MARCOS RUEDA LLORENTE</div>
      <div class="person__role">COMERCIAL</div>
    </div>
    <ul class="contact contact--postal">
      <li><svg viewBox="0 0 12 12"><circle class="icon-disc" cx="6" cy="6" r="6"/><path class="icon-glyph" d="M6 9.5 C4 7 3.6 6 3.6 5 a2.4 2.4 0 0 1 4.8 0 c0 1-.4 2-2.4 4.5z"/></svg><span class="wide">Pol. Ind. Norvalle - C/4 Nº 22</span></li>
      <li><span class="no-icon"></span><span>41720 VILLANORTE DEL RÍO (Sevilla)</span></li>
      <li><svg viewBox="0 0 12 12"><circle class="icon-disc" cx="6" cy="6" r="6"/><path class="icon-glyph" d="M3.2 4h5.6v4H3.2z M3.2 4 6 6.3 8.8 4"/></svg><span class="wider">Apartado de Correos 254</span></li>
      <li><svg viewBox="0 0 12 12"><circle class="icon-disc" cx="6" cy="6" r="6"/><circle class="icon-glyph" cx="6" cy="6" r="1.5"/><path class="icon-glyph" d="M7.5 4.5v2.3c0 .9 1.3.9 1.3-.6A2.8 2.8 0 1 0 7.6 8.4"/></svg><span class="wider">marcosrueda@travenic.com</span></li>
    </ul>
    <ul class="contact contact--direct">
      <li><svg viewBox="0 0 12 12"><circle class="icon-disc" cx="6" cy="6" r="6"/><rect class="icon-glyph" x="4.2" y="2.7" width="3.6" height="6.6" rx=".6"/></svg><span class="wide">611 48 27 53</span></li>
      <li><svg viewBox="0 0 12 12"><circle class="icon-disc" cx="6" cy="6" r="6"/><path class="icon-glyph" d="M4 3c-1 .8-.8 2.4.6 4s3 2.1 3.9 1.2L7.5 7l-.9.5C5.8 7 5 6.2 4.6 5.3l.6-.8z"/></svg><span class="wide">954 72 18 40</span></li>
      <li><svg viewBox="0 0 12 12"><circle class="icon-disc" cx="6" cy="6" r="6"/><path class="icon-glyph" d="M4.2 5V3h3.6v2 M3 5h6v3H3z M4.2 7.3h3.6V9H4.2z"/></svg><span class="wide">954 72 18 41</span></li>
      <li><svg viewBox="0 0 12 12"><circle class="icon-disc" cx="6" cy="6" r="6"/><circle class="icon-glyph" cx="6" cy="6" r="3"/><path class="icon-glyph" d="M3 6h6 M6 3c-1.5 2-1.5 4 0 6 M6 3c1.5 2 1.5 4 0 6"/></svg><span>www.travenic.com</span></li>
    </ul>
  </section>

  <p class="version-label version-label--1">Version 1</p>
  <p class="version-label version-label--2">Version 2</p>
</main>
</body>
</html>
```